Vesprine Oakville Cabernet Sauvignon-Wine label design

We need a package design for an up market wine brand named, Vesprine. It will be a Cabernet Sauvignon from the Oakville AVA of Napa Valley. We are looking for a stylish modern label that will stand out on a retail shelf. We want the label to be attention grabbing and stylish while presenting an up market luxury brand.

Sick

Requirements
Must have
• Must have the words(in order of importance)
-Vesprine
-Cabernet Sauvignon
-Oakville
-Napa Valley
-2018

Must be designed for a traditional "Bordeaux" style bottle (Bottle specs in uploaded files)
Should not have
• Any images of grapes, vineyards, wine glasses or bottles

```html
<!DOCTYPE html>
<html lang="en">
<head>
<meta charset="utf-8">
<title>Vesprine Oakville Cabernet Sauvignon Label</title>
<link rel="stylesheet" href="https://fonts.googleapis.com/css2?family=Josefin+Sans:wght@300;400&display=swap">
<style>
  :root {
    --backdrop: #484848;
    --paper: #ffffff;
    --ink: #1a1a1a;
    --gold: #c9932f;
    --gold-light: #e2b24a;
    --night: #14112e;
    --violet: #4a1f8c;
    --indigo: #2a2f8a;
    --magenta: #9b2aa8;
    --sky: #6fa3e6;
    --type: "Josefin Sans", sans-serif;
  }
  * { box-sizing: border-box; margin: 0; padding: 0; }
  html, body {
    width: 1200px; height: 1200px; overflow: hidden;
    background: var(--backdrop);
  }
  .canvas {
    position: relative; width: 1200px; height: 1200px;
    display: flex; align-items: center; justify-content: center;
  }
  .label {
    position: relative; width: 540px; height: 1040px;
    background: var(--paper);
    border-radius: 4px;
    overflow: hidden;
  }
  .label__art {
    position: absolute; left: 0; top: 0; width: 100%; height: 800px;
    background:
      radial-gradient(ellipse 160px 220px at 22% 62%, var(--sky) 0%, transparent 70%),
      radial-gradient(ellipse 200px 180px at 72% 85%, var(--magenta) 0%, transparent 72%),
      radial-gradient(ellipse 220px 160px at 30% 12%, var(--night) 0%, transparent 70%),
      radial-gradient(ellipse 260px 300px at 80% 30%, var(--violet) 0%, transparent 75%),
      linear-gradient(160deg, var(--indigo) 0%, var(--violet) 50%, #5a1f7a 100%);
  }
  .brand-plate {
    position: absolute; left: 38px; top: 380px; width: 410px; height: 190px;
    background: rgba(16, 13, 38, 0.88);
    display: flex; flex-direction: column; align-items: center; justify-content: center;
  }
  .brand-plate__frame {
    position: absolute; inset: 14px;
    border: 1.5px solid var(--gold);
  }
  .brand-plate__name {
    position: relative;
    font-family: var(--type); font-weight: 300;
    font-size: 64px; letter-spacing: 0.04em;
    color: var(--gold-light);
  }
  .brand-plate__region {
    position: relative; margin-top: 14px;
    font-family: var(--type); font-weight: 400;
    font-size: 15px; letter-spacing: 0.42em;
    color: #e8e4f2;
  }
  .varietal {
    position: absolute; left: 0; bottom: 0; width: 100%; height: 240px;
    display: flex; flex-direction: column; align-items: center; justify-content: center;
    font-family: var(--type); font-weight: 400;
  }
  .varietal__name {
    font-size: 26px; letter-spacing: 0.55em; line-height: 1.5;
    color: var(--gold); text-align: center; padding-left: 0.55em;
  }
  .varietal__vintage {
    margin-top: 18px;
    font-size: 24px; letter-spacing: 0.6em; padding-left: 0.6em;
    color: var(--ink);
  }
</style>
</head>
<body>
  <main class="canvas">
    <section class="label">
      <div class="label__art" role="img" aria-label="Marbled fluid-art pattern in deep purple, indigo, magenta and sky blue with gold veining"></div>
      <div class="brand-plate">
        <div class="brand-plate__frame"></div>
        <h1 class="brand-plate__name">Vesprine</h1>
        <p class="brand-plate__region">OAKVILLE • NAPA VALLEY</p>
      </div>
      <div class="varietal">
        <p class="varietal__name">CABERNET<br>SAUVIGNON</p>
        <p class="varietal__vintage">2018</p>
      </div>
    </section>
  </main>
</body>
</html>
```